Larkmoor Business Card Design Project

Double side card , just the logo on oxford white background on one side , and the rest of the information on the other side..
the company name is : Larkmoor Continental General Trading LLC.
logo is already attached
the card to show in the info side: company name, employee name and position (job title) phone number, fax number, email address, P.O. box, Location (city and country)
deadline is already extended 4 all to have more time... thanks

```html
<!DOCTYPE html>
<html lang="en">
<head>
<meta charset="utf-8">
<title>Larkmoor Continental – Business Card</title>
<link rel="stylesheet" href="https://fonts.googleapis.com/css2?family=Open+Sans:wght@400;600;700&display=swap">
<style>
  :root {
    --backdrop: #3a3a3c;
    --card-white: #fbfbfa;
    --ink-grey: #7a7a7c;
    --ink-dark: #6b6b6d;
    --accent-blue: #3a9fd0;
    --logo-grey: #6e6e70;
  }
  * { margin: 0; padding: 0; box-sizing: border-box; }
  html, body {
    width: 1200px;
    height: 900px;
    overflow: hidden;
    background: var(--backdrop);
    font-family: "Open Sans", Arial, sans-serif;
  }
  .card-set {
    position: relative;
    width: 1200px;
    height: 900px;
  }
  .card {
    position: absolute;
    top: 300px;
    width: 525px;
    height: 300px;
    background: var(--card-white);
    box-shadow: 0 12px 30px rgba(0,0,0,0.45);
  }
  .card--front { left: 50px; }
  .card--back  { left: 625px; }

  /* Front side */
  .brand {
    position: absolute;
    left: 0; right: 0;
    top: 112px;
    display: flex;
    align-items: center;
    justify-content: center;
    gap: 12px;
  }
  .brand__dot {
    width: 14px; height: 14px;
    border-radius: 50%;
    background: var(--accent-blue);
  }
  .brand__name {
    font-size: 40px;
    font-weight: 600;
    letter-spacing: 2px;
    color: var(--logo-grey);
    text-transform: uppercase;
  }
  .website {
    position: absolute;
    left: 0; right: 0;
    top: 180px;
    text-align: center;
    font-size: 15px;
    letter-spacing: 2px;
    color: var(--ink-grey);
  }
  .website strong { font-weight: 700; }

  /* Back side */
  .identity {
    position: absolute;
    right: 290px;
    top: 118px;
    text-align: right;
  }
  .identity__name {
    font-size: 21px;
    font-weight: 700;
    color: var(--ink-grey);
    letter-spacing: 0.3px;
    white-space: nowrap;
  }
  .identity__role {
    margin-top: 4px;
    font-size: 15px;
    color: var(--accent-blue);
  }
  .divider {
    position: absolute;
    left: 250px;
    top: 62px;
    width: 2px;
    height: 168px;
    background: var(--accent-blue);
  }
  .contact {
    position: absolute;
    left: 266px;
    top: 60px;
    font-size: 14px;
    line-height: 21px;
    color: var(--ink-dark);
    white-space: nowrap;
  }
  .contact__line {
    display: flex;
    align-items: center;
    gap: 8px;
  }
  .contact__icon { width: 13px; display: flex; justify-content: center; }
  .contact__address { margin-top: 8px; }
  .company-name {
    position: absolute;
    left: 0; right: 0;
    bottom: 26px;
    text-align: center;
    font-size: 13px;
    font-weight: 600;
    letter-spacing: 1px;
    color: var(--ink-grey);
  }
</style>
</head>
<body>
<main class="card-set">
  <section class="card card--front" aria-label="Card front">
    <div class="brand">
      <span class="brand__dot"></span>
      <span class="brand__name">Larkmoor</span>
    </div>
    <p class="website">www.<strong>larkmoor</strong>.com</p>
  </section>

  <section class="card card--back" aria-label="Card back">
    <div class="identity">
      <p class="identity__name">DANIEL HARTWELL</p>
      <p class="identity__role">director</p>
    </div>
    <div class="divider"></div>
    <div class="contact">
      <p class="contact__line">
        <span class="contact__icon">
          <svg width="12" height="12" viewBox="0 0 12 12" aria-label="Phone">
            <path d="M2 1 L4 1 L5 4 L3.5 5 Q5 8 7 8.5 L8 7 L11 8 L11 10 Q10 11 8.5 11 Q2 9 1 2.5 Q1 1.5 2 1 Z" fill="var(--accent-blue)"/>
          </svg>
        </span>
        <span>555.010.4821</span>
      </p>
      <p class="contact__line">
        <span class="contact__icon">
          <svg width="13" height="12" viewBox="0 0 13 12" aria-label="Fax">
            <rect x="3" y="0.5" width="7" height="4" fill="none" stroke="var(--accent-blue)" stroke-width="1.2"/>
            <rect x="1" y="4" width="11" height="7.5" rx="1" fill="var(--accent-blue)"/>
            <rect x="3" y="6" width="7" height="1.2" fill="var(--card-white)"/>
          </svg>
        </span>
        <span>555.010.4822</span>
      </p>
      <p>daniel@larkmoor.com</p>
      <p class="contact__address">880 W. Linden Avenue - Suite 210<br>P.O. Box 4417<br>Port Calder, SC 29410, USA</p>
    </div>
    <p class="company-name">Larkmoor Continental General Trading LLC.</p>
  </section>
</main>
</body>
</html>
```